Suds Harbor Laundromat Wordpress Design

We need a Wordpress website design for our laundromat, Suds Harbor Atlanta, at www.sudsharboratlanta-example.com. We would like to have 6 pages: Home, About Us, Services, Locations, Reviews and Contact us. We will provide content for the text on each page. What we do: We are a full service laundromat that provides dry cleaning drop off, professional laundry services, wash dry fold and self service laundry to the local community. We would like to use the color scheme from our logo to convey a warm, safe, and bright business that caters to its diverse community.
Updates

I like the structure of this laundromat website: http://www.tumblewashhub-example.com/ Using my logo and color scheme in the above referenced website is what. Am looking for. The photos attached to the project with the female model should be used as a primary focus and supplemented by actual photos of the equipment.

Target Market(s)

Our target market is a diverse group of people from Midtown Atlanta - LGBTQ community /Locals/Regulars that have been coming to laundromat for 30 years.

Industry/Entity Type

Laundromat

Coding

Coded - Design and coding required

Number of Pages Required

5+ page

Font styles to use
Sans Serif

Colors
0054AA
0677BA
7BADD7
CADEEF
E8F1F8

Requirements
Must have
• Feature this video on the main page: https://video.example.com/Qx7mBr2Lp0Z

```html
<!DOCTYPE html>
<html lang="en">
<head>
<meta charset="utf-8">
<title>Suds Harbor Laundromat</title>
<link href="https://fonts.googleapis.com/css2?family=Figtree:ital,wght@0,400;0,500;0,600;0,700;1,400&family=Lobster+Two:ital,wght@1,700&display=swap" rel="stylesheet">
<style>
:root{
  --red:#cc0a0a;
  --navy:#053069;
  --navy-deep:#02306a;
  --cyan:#e0fcfc;
  --page:#f5f6f8;
  --grey:#8a8f99;
  --white:#fff;
  --input:#5f7b9c;
}
*{margin:0;padding:0;box-sizing:border-box}
html,body{width:1200px;height:2585px;overflow:hidden}
body{position:relative;background:var(--page);font-family:'Figtree',sans-serif;color:var(--navy)}
.abs{position:absolute}
.script{font-family:'Lobster Two',cursive;font-style:italic;font-weight:700}

/* header */
.site-header{left:0;top:0;width:1200px;height:75px;background:var(--cyan)}
.brand{left:88px;top:20px;font-size:28px;font-weight:700;color:var(--red);letter-spacing:.2px}
.brand-dot{display:inline-block;width:14px;height:14px;border-radius:50%;background:var(--red);margin-right:8px;vertical-align:2px}
.main-nav{left:471px;top:30px;display:flex;gap:21px;font-size:13px;font-weight:500;color:#1c2430}
.main-nav .active{color:var(--red)}
.header-phone{left:820px;top:27px;display:flex;align-items:center;gap:6px;font-size:16px;font-weight:700;font-style:italic;color:var(--red)}
.btn{display:flex;align-items:center;justify-content:center;font-size:12.5px;font-weight:600;border:1px solid;background:transparent}
.btn-contact{left:962px;top:18px;width:113px;height:38px;color:var(--red);border-color:var(--red);background:var(--white)}

/* hero */
.hero{left:0;top:75px}
.hero-title{left:0;top:368px;width:1172px;text-align:center;font-size:38px;color:var(--white)}
.hero-sub{left:340px;top:417px;width:490px;text-align:center;font-size:22px;line-height:27px;color:var(--white)}

/* what we do */
.section-title{left:0;width:1200px;text-align:center;font-size:40px;color:var(--navy)}
.service{top:733px;width:250px;text-align:center}
.service-photo{width:200px;height:200px;border-radius:50%;border:1px solid var(--red);margin:0 auto;padding:4px}
.service-photo div{width:100%;height:100%;border-radius:50%;background:linear-gradient(150deg,#d9dcd8,#a8b3b6 55%,#4f7fb8)}
.service h3{margin-top:14px;font-size:16.5px;font-weight:700;color:var(--navy)}
.service p{margin-top:14px;font-size:10.5px;line-height:15px;color:var(--grey)}
.service .btn{margin:21px auto 0;width:113px;height:38px;color:var(--navy);border-color:var(--navy)}
.service .btn.hot{color:var(--red);border-color:var(--red)}

/* about band */
.about-band{left:0;top:1210px;width:1200px;height:486px;background:var(--navy-deep)}
.about-title{left:88px;top:1290px;font-size:38px;line-height:51px;color:var(--white)}
.about-text{left:88px;top:1405px;width:635px;font-size:10.5px;line-height:15px;color:var(--white)}
.checks{top:1468px;list-style:none;color:var(--white);font-size:11.5px;font-weight:700}
.checks li{display:flex;align-items:center;gap:9px;height:19px}
.btn-about{left:88px;top:1567px;width:113px;height:38px;color:var(--white);border-color:var(--white)}
.video-frame{left:773px;top:1272px;width:336px;height:336px;border:1px solid var(--red)}
.video{left:748px;top:1297px;width:336px;height:336px;background:linear-gradient(160deg,#8c8f88,#b9b0a2 45%,#6f6f72)}

/* reviews */
.review{top:1817px;width:249px;height:274px;background:var(--white);box-shadow:0 2px 12px rgba(0,30,80,.07);padding:26px 18px}
.review p{margin-top:14px;font-size:10.5px;line-height:19px;font-style:italic;color:var(--grey)}
.review h4{margin-top:13px;font-size:12px;font-weight:700;color:var(--navy)}
.review span{font-size:10.5px;color:var(--navy)}

/* footer */
.footer-bg{left:0;top:2150px}
.footer-brand{left:200px;top:2360px;font-size:26px;font-weight:700;color:var(--red)}
.foot-h{font-size:15px;color:var(--navy)}
.foot-list{list-style:none;font-size:10.5px;color:var(--navy)}
.contact-row{display:flex;gap:10px;align-items:flex-start;font-size:10.5px;line-height:15px;color:var(--navy)}
.newsletter-input{left:816px;top:2400px;width:181px;height:25px;background:var(--input);color:#e4ebf3;font-size:9px;padding:7px 12px}
.btn-news{left:816px;top:2437px;width:100px;height:26px;color:var(--red);border-color:var(--red)}
.divider{left:200px;top:2512px;width:797px;height:1px;background:#c7dbe0}
.copyright{left:200px;top:2535px;font-size:9.5px;color:var(--grey)}
.copyright b{color:var(--red);font-weight:600}
.social{top:2530px;width:24px;height:24px;border-radius:50%}
</style>
</head>
<body>

<header class="abs site-header">
  <div class="abs brand"><span class="brand-dot"></span>Suds Harbor</div>
  <nav class="abs main-nav">
    <span class="active">Home</span><span>About Us</span><span>Services</span><span>Locations</span><span>Reviews</span>
  </nav>
  <div class="abs header-phone">
    <svg width="16" height="16" viewBox="0 0 24 24" fill="none" stroke="currentColor" stroke-width="2"><path d="M22 16.9v3a2 2 0 0 1-2.2 2 19.8 19.8 0 0 1-8.6-3.1 19.5 19.5 0 0 1-6-6A19.8 19.8 0 0 1 2.1 4.2 2 2 0 0 1 4.1 2h3a2 2 0 0 1 2 1.7c.1.9.4 1.8.7 2.7a2 2 0 0 1-.5 2.1L8 9.8a16 16 0 0 0 6 6l1.3-1.3a2 2 0 0 1 2.1-.4c.9.3 1.8.6 2.7.7a2 2 0 0 1 1.7 2z"/></svg>
    404-555-0147
  </div>
  <div class="abs btn btn-contact">Contact Us</div>
</header>

<svg class="abs hero" width="1200" height="545" viewBox="0 75 1200 545" role="img" aria-label="Laundromat interior with a row of front-loading washers and a woman in a blue dress">
  <defs>
    <linearGradient id="heroFill" x1="0" y1="0" x2="0" y2="1">
      <stop offset="0" stop-color="#6d7c7b"/>
      <stop offset=".5" stop-color="#8f9894"/>
      <stop offset="1" stop-color="#5b6468"/>
    </linearGradient>
  </defs>
  <path d="M0 75H1200V468C900 470 800 588 600 588C400 588 300 470 0 468Z" fill="url(#heroFill)"/>
  <path d="M0 468C300 470 400 588 600 588C800 588 900 470 1200 468V474C900 478 800 612 600 612C400 612 300 478 0 474Z" fill="var(--red)"/>
  <path d="M600 535V553M593 546L600 553L607 546" stroke="#fff" stroke-width="1.6" fill="none"/>
</svg>
<div class="abs hero-title script">Laundromat for 30 Years</div>
<div class="abs hero-sub">Coin Laundry, Dry Cleaning, and Professional Laundry</div>

<h2 class="abs section-title script" style="top:664px">What We Do</h2>

<div class="abs service" style="left:199px">
  <div class="service-photo"><div role="img" aria-label="Woman beside front-loading washers"></div></div>
  <h3>Dry Cleaning Drop Off</h3>
  <p>It is a long established fact that a reader will be distracted by the readable content of a page when looking at its layout. The point of using Lorem Ipsum is that it has a more-or-less normal ...</p>
  <div class="btn">Read More</div>
</div>
<div class="abs service" style="left:473px">
  <div class="service-photo"><div role="img" aria-label="Woman seated in front of a row of washers"></div></div>
  <h3>Professional Laundry Services</h3>
  <p>It is a long established fact that a reader will be distracted by the readable content of a page when looking at its layout. The point of using Lorem Ipsum is that it has a more-or-less normal ...</p>
  <div class="btn hot">Read More</div>
</div>
<div class="abs service" style="left:747px">
  <div class="service-photo"><div role="img" aria-label="Woman standing under the laundromat sign"></div></div>
  <h3>Wash Dry Fold</h3>
  <p>It is a long established fact that a reader will be distracted by the readable content of a page when looking at its layout. The point of using Lorem Ipsum is that it has a more-or-less normal ...</p>
  <div class="btn">Read More</div>
</div>

<svg class="abs" style="left:0;top:1176px" width="1200" height="36"><path d="M0 2L600 34H0Z" fill="var(--red)"/></svg>
<section class="abs about-band"></section>
<svg class="abs" style="left:0;top:1695px" width="1200" height="32"><path d="M600 0H1200V31Z" fill="var(--red)"/></svg>

<h2 class="abs about-title script">Coin Laundry, Dry Cleaning, &amp;<br>Professional Laundry</h2>
<p class="abs about-text">There are many variations of passages of Lorem Ipsum available, but the majority have suffered alteration in some form, by injected humour, or randomised words which don't look even slightly believable. If you are going to use a passage of Lorem Ipsum, you need to be sure there isn't anything embarrassing hidden in the middle of text.</p>
<ul class="abs checks" style="left:88px">
  <li><svg width="13" height="9" viewBox="0 0 13 9" fill="none" stroke="#fff" stroke-width="1.3"><path d="M1 5l3 3 8-7M5 5l3-3"/></svg>In Business over 45 years</li>
  <li><svg width="13" height="9" viewBox="0 0 13 9" fill="none" stroke="#fff" stroke-width="1.3"><path d="M1 5l3 3 8-7M5 5l3-3"/></svg>Voted "BEST COIN LAUNDRY" - Multiple years</li>
  <li><svg width="13" height="9" viewBox="0 0 13 9" fill="none" stroke="#fff" stroke-width="1.3"><path d="M1 5l3 3 8-7M5 5l3-3"/></svg>The best Wash-Dry-Fold in town</li>
  <li><svg width="13" height="9" viewBox="0 0 13 9" fill="none" stroke="#fff" stroke-width="1.3"><path d="M1 5l3 3 8-7M5 5l3-3"/></svg>Over 50 well maintained machines</li>
</ul>
<ul class="abs checks" style="left:380px">
  <li><svg width="13" height="9" viewBox="0 0 13 9" fill="none" stroke="#fff" stroke-width="1.3"><path d="M1 5l3 3 8-7M5 5l3-3"/></svg>In Business over 45 years</li>
  <li><svg width="13" height="9" viewBox="0 0 13 9" fill="none" stroke="#fff" stroke-width="1.3"><path d="M1 5l3 3 8-7M5 5l3-3"/></svg>One of Atlanta's First, Finest, &amp; Friendliest Coin Laundries</li>
  <li><svg width="13" height="9" viewBox="0 0 13 9" fill="none" stroke="#fff" stroke-width="1.3"><path d="M1 5l3 3 8-7M5 5l3-3"/></svg>Cool - Comfortable - Clean</li>
  <li><svg width="13" height="9" viewBox="0 0 13 9" fill="none" stroke="#fff" stroke-width="1.3"><path d="M1 5l3 3 8-7M5 5l3-3"/></svg>Commercial Accounts</li>
</ul>
<div class="abs btn btn-about">About Us</div>
<div class="abs video-frame"></div>
<div class="abs video" role="img" aria-label="Video still of a customer carrying a laundry basket inside the laundromat"></div>
<svg class="abs" style="left:899px;top:1448px" width="36" height="36" viewBox="0 0 36 36"><circle cx="18" cy="18" r="16" fill="none" stroke="#fff" stroke-width="2"/><path d="M14 11L25 18L14 25Z" fill="#fff"/></svg>

<h2 class="abs section-title script" style="top:1748px">Client Reviews</h2>

<div class="abs review" style="left:200px">
  <svg width="30" height="18" viewBox="0 0 30 18" fill="none" stroke="var(--red)" stroke-width="2.2"><path d="M11 2H5L2 9v7h9V9H3M27 2h-6l-3 7v7h9V9h-8"/></svg>
  <p>"There are many variations of passages of Lorem Ipsum available, but the majority have suffered alteration in some form, by injected humour, or randomised words which don't look even slightly believable. If you are going to use a passage of Lorem Ipsum, you need to be sure there isn't anything embarrassing"</p>
  <h4>Standard Chunk</h4><span>popular belief</span>
</div>
<div class="abs review" style="left:474px">
  <svg width="30" height="18" viewBox="0 0 30 18" fill="none" stroke="var(--red)" stroke-width="2.2"><path d="M11 2H5L2 9v7h9V9H3M27 2h-6l-3 7v7h9V9h-8"/></svg>
  <p>"There are many variations of passages of Lorem Ipsum available, but the majority have suffered alteration in some form, by injected humour, or randomised words which don't look even slightly believable. If you are going to use a passage of Lorem Ipsum, you need to be sure there isn't anything embarrassing"</p>
  <h4>Standard Chunk</h4><span>popular belief</span>
</div>
<div class="abs review" style="left:748px">
  <svg width="30" height="18" viewBox="0 0 30 18" fill="none" stroke="var(--red)" stroke-width="2.2"><path d="M11 2H5L2 9v7h9V9H3M27 2h-6l-3 7v7h9V9h-8"/></svg>
  <p>"There are many variations of passages of Lorem Ipsum available, but the majority have suffered alteration in some form, by injected humour, or randomised words which don't look even slightly believable. If you are going to use a passage of Lorem Ipsum, you need to be sure there isn't anything embarrassing"</p>
  <h4>Standard Chunk</h4><span>popular belief</span>
</div>

<svg class="abs footer-bg" width="1200" height="435" viewBox="0 2150 1200 435">
  <path d="M0 2290C300 2290 400 2160 600 2160C800 2160 900 2290 1200 2290V2585H0Z" fill="var(--cyan)"/>
  <path d="M0 2290C300 2290 400 2160 600 2160C800 2160 900 2290 1200 2290V2293C900 2293 800 2185 600 2185C400 2185 300 2293 0 2293Z" fill="var(--red)"/>
  <path d="M0 2288H1200V2292H0Z" fill="var(--red)" opacity=".9"/>
  <path d="M600 2236V2218M593 2225L600 2218L607 2225" stroke="var(--red)" stroke-width="1.6" fill="none"/>
</svg>

<div class="abs footer-brand"><span class="brand-dot"></span>Suds Harbor</div>

<div class="abs" style="left:405px;top:2325px">
  <div class="foot-h script">Contact Us</div>
  <div class="contact-row" style="margin-top:14px;font-size:14px">
    <svg width="13" height="13" viewBox="0 0 24 24" fill="none" stroke="var(--red)" stroke-width="2"><path d="M22 16.9v3a2 2 0 0 1-2.2 2 19.8 19.8 0 0 1-8.6-3.1 19.5 19.5 0 0 1-6-6A19.8 19.8 0 0 1 2.1 4.2 2 2 0 0 1 4.1 2h3a2 2 0 0 1 2 1.7c.1.9.4 1.8.7 2.7a2 2 0 0 1-.5 2.1L8 9.8a16 16 0 0 0 6 6l1.3-1.3a2 2 0 0 1 2.1-.4c.9.3 1.8.6 2.7.7a2 2 0 0 1 1.7 2z"/></svg>(404) 555-0147</div>
  <div class="contact-row" style="margin-top:6px">
    <svg width="12" height="12" viewBox="0 0 24 24" fill="none" stroke="var(--red)" stroke-width="2"><rect x="3" y="5" width="18" height="14" rx="2"/><path d="M3 7l9 6 9-6"/></svg>hello@sudsharbor-example.com</div>
  <div class="contact-row" style="margin-top:14px">
    <svg width="12" height="14" viewBox="0 0 24 28" fill="none" stroke="var(--red)" stroke-width="2"><path d="M12 26s9-9 9-15a9 9 0 0 0-18 0c0 6 9 15 9 15z"/><circle cx="12" cy="11" r="3"/></svg>
    <span>Harbor Point Plaza,<br>1200 Example Ave NE., # 210, Atlanta,<br>GA 30300</span></div>
</div>

<div class="abs" style="left:667px;top:2325px">
  <div class="foot-h script">Quick Links</div>
  <ul class="foot-list" style="margin-top:10px;line-height:19px">
    <li>Home</li><li>About Us</li><li>Services</li><li>Locations</li><li>Reviews</li><li>Contact Us</li>
  </ul>
</div>

<div class="abs" style="left:816px;top:2325px;width:185px">
  <div class="foot-h script">Sign Up Newsletter</div>
  <p style="margin-top:10px;font-size:10px;line-height:15px;color:var(--navy)">There are many variations of passages lorem Ipsum available</p>
</div>
<div class="abs newsletter-input">Enter your email ...</div>
<div class="abs btn btn-news">Read More</div>

<div class="abs divider"></div>
<div class="abs copyright">© 2021 <b>Suds Harbor Atlanta</b> All Right Reserved</div>
<div class="abs social" style="left:817px;background:var(--navy)" role="img" aria-label="Social profile link"></div>
<div class="abs social" style="left:848px;background:var(--red)" role="img" aria-label="Social profile link"></div>

</body>
</html>
```